Copper Gavel Auctions business card design with existing logo

Looking for a sleek and sexy design using our current logo

Contact Information for Business Card

Name, address, email, phone, website. Marcus Delvane 418 Birchmont Road Suite 200C Fenwick NY 11093 Copperbidhouse.net (631)582-4067

```html
<!DOCTYPE html>
<html lang="en">
<head>
<meta charset="utf-8">
<title>Copper Gavel Auctions – Business Card</title>
<link rel="stylesheet" href="https://fonts.googleapis.com/css2?family=Michroma&display=swap">
<style>
  :root {
    --backdrop: #2a2624;
    --card: #171717;
    --red: #d41a24;
    --blue: #1c4595;
    --rule: #3a3a3a;
  }
  * { box-sizing: border-box; margin: 0; padding: 0; }
  html, body {
    width: 1200px; height: 842px; overflow: hidden;
    background: var(--backdrop);
  }
  .stage {
    position: relative; width: 1200px; height: 842px;
    display: flex; align-items: center; justify-content: center; gap: 60px;
  }
  .card {
    position: relative; width: 500px; height: 286px;
    background: var(--card);
    font-family: "Michroma", "Eurostile", sans-serif;
    font-variant: small-caps;
    overflow: hidden;
  }

  /* contact side */
  .band { position: absolute; left: 0; right: 0; height: 14px; background: var(--red); }
  .band::after {
    content: ""; position: absolute; left: 0; right: 0; height: 2px; background: var(--blue);
  }
  .band--top { top: 0; }
  .band--top::after { bottom: -2px; }
  .band--bottom { bottom: 0; }
  .band--bottom::after { top: -2px; }

  .contact {
    position: absolute; inset: 16px 0;
    display: flex; flex-direction: column; align-items: center; justify-content: center;
    text-align: center; letter-spacing: 2px;
  }
  .contact__name { color: var(--red); font-size: 17px; letter-spacing: 3px; }
  .contact__rule { width: 110px; height: 1px; background: var(--rule); margin: 12px 0; }
  .contact__line { color: var(--blue); font-size: 12px; line-height: 1.6; }
  .contact__web span { color: var(--red); }

  /* logo side */
  .tab { position: absolute; width: 40px; height: 44px; background: var(--red); }
  .tab::before { content: ""; position: absolute; top: 0; bottom: 0; width: 3px; background: var(--blue); }
  .tab--left { left: 0; top: 170px; }
  .tab--left::before { right: -6px; }
  .tab--right { right: 0; top: 52px; }
  .tab--right::before { left: -6px; }

  .brand {
    position: absolute; inset: 0;
    display: flex; flex-direction: column; align-items: center; justify-content: center;
  }
  .brand__mark { width: 46px; height: 46px; border-radius: 50%; background: var(--blue); margin-bottom: 14px; }
  .brand__name { color: var(--red); font-size: 21px; letter-spacing: 1px; }
  .brand__tagline {
    display: flex; align-items: center; gap: 10px; margin-top: 10px;
    color: var(--blue); font-size: 13px; letter-spacing: 3px;
  }
  .brand__tagline::before, .brand__tagline::after {
    content: ""; width: 36px; height: 2px; background: var(--blue);
  }
</style>
</head>
<body>
<main class="stage">
  <section class="card card--contact">
    <div class="band band--top"></div>
    <div class="contact">
      <p class="contact__name">Marcus Delvane</p>
      <div class="contact__rule"></div>
      <p class="contact__line">418 Birchmont Road Suite 200C</p>
      <p class="contact__line">Fenwick NY 11093</p>
      <div class="contact__rule"></div>
      <p class="contact__line">(631)582-4067</p>
      <p class="contact__line">info@copperbidhouse.net</p>
      <p class="contact__line contact__web">www.<span>Copperbidhouse.net</span></p>
    </div>
    <div class="band band--bottom"></div>
  </section>

  <section class="card card--brand">
    <div class="tab tab--right"></div>
    <div class="tab tab--left"></div>
    <div class="brand">
      <div class="brand__mark"></div>
      <p class="brand__name">Copper Gavel Auctions</p>
      <p class="brand__tagline">Buy-Sell-Consign</p>
    </div>
  </section>
</main>
</body>
</html>
```